website for Velunora.de

In Naturheilzentrum VELUNORA, the medical team using the Advanced Laboratory examines the health status of patients and each patient is treated with special care in Germany. Multi language.
The design must show mix of modern medical service.
pages :
1. Home
2. Philosophie
3.Diagnose
4. Therapie
5. Kontakt
6.über uns
7. Zentrum ( Bilder )
8.Unser Ergebnisse
9. Anfahrt

Target Market(s)

International

Industry/Entity Type

Hospital

Font styles to use
Decorative

Colors
0455a3

Requirements
Must have
• The design must show mix of modern medical service.
• Advanced Laboratory abilities.
Nice to have
• Medical Theme
• for blue color reference see the attachment 1.jpeg

```html
<!DOCTYPE html>
<html lang="en">
<head>
<meta charset="utf-8">
<title>Velunora – Naturheilzentrum</title>
<link href="https://fonts.googleapis.com/css2?family=Cinzel:wght@400;700&family=Open+Sans:wght@400;600;700&display=swap" rel="stylesheet">
<style>
:root{
  --blue:#0455a3;
  --green:#8cc63f;
  --green-dark:#6db33f;
  --ink:#222;
  --text:#555;
  --muted:#888;
  --grey-band:#f1f0f0;
  --line:#e3e3e3;
  --white:#fff;
}
*{box-sizing:border-box;margin:0;padding:0}
html,body{width:1200px;height:3203px;overflow:hidden;background:var(--white)}
body{position:relative;font-family:"Open Sans",Arial,sans-serif;color:var(--text)}
.abs{position:absolute}
.btn{position:absolute;display:flex;align-items:center;justify-content:center;background:var(--green);color:var(--white);font:700 15px "Open Sans",Arial,sans-serif;border-radius:22px;letter-spacing:.3px}

/* header */
.brand{position:absolute;left:98px;top:22px;display:flex;align-items:center;gap:12px}
.brand-mark{width:34px;height:34px;background:var(--green-dark)}
.brand-name{font:700 36px "Cinzel",Georgia,serif;color:var(--green-dark)}
.contact-item{position:absolute;top:28px;display:flex;align-items:center;gap:14px;font-size:17px;color:#333}
.contact-item b{color:var(--blue);font-weight:600}
.ring{width:38px;height:38px;border:2px solid var(--green);border-radius:50%;display:flex;align-items:center;justify-content:center}
.main-nav{position:absolute;left:0;top:107px;width:1200px;height:43px;background:var(--blue);display:flex;justify-content:space-between;align-items:center;padding:0 84px 0 94px}
.main-nav a{font:400 17px "Cinzel",Georgia,serif;color:var(--white);text-decoration:none}

/* hero */
.hero{position:absolute;left:0;top:150px;width:1200px;height:491px;background:linear-gradient(110deg,#1f6fb0 0%,#5aa3d6 30%,#c9dbe8 55%,#8ea7ba 75%,#4d6b84 100%)}
.hero-title{position:absolute;left:687px;top:92px;font:700 54px/1.38 "Cinzel",Georgia,serif;color:var(--white);letter-spacing:1px}
.hero-btn{left:687px;top:341px;width:248px;height:48px;background:var(--green);border:2px solid var(--white);border-radius:24px;font-size:16px}
.slide-arrow{position:absolute;top:223px;width:42px;height:50px;background:rgba(120,120,120,.75);display:flex;align-items:center;justify-content:center}

/* welcome */
.welcome-box{position:absolute;left:98px;top:730px;width:613px;height:393px;border:2px solid #6b8fc4}
.welcome-title{position:absolute;left:143px;top:774px;font:400 32px "Cinzel",Georgia,serif;color:var(--ink);white-space:nowrap}
.welcome-text{position:absolute;left:143px;top:836px;width:450px;font-size:13px;line-height:27px;color:var(--text);white-space:nowrap}
.welcome-media{position:absolute;left:626px;top:764px;width:474px;height:325px;background:linear-gradient(135deg,#0a2d5a,#2d6da8 45%,#b9d3e6 80%,#e6eef5)}
.play{position:absolute;left:830px;top:895px;width:64px;height:64px;border-radius:50%;background:#111;display:flex;align-items:center;justify-content:center}

/* features */
.feature-band{position:absolute;left:0;top:1217px;width:1200px;height:498px;background:var(--grey-band)}
.feature{position:absolute;top:1305px;width:330px;text-align:center}
.feature-icon{width:106px;height:106px;border-radius:50%;background:var(--blue);margin:0 auto;display:flex;align-items:center;justify-content:center}
.feature h3{font:400 23px "Cinzel",Georgia,serif;color:var(--ink);margin-top:34px}
.feature p{font-size:14px;line-height:22px;margin:16px 15px 0}
.feature .btn{position:relative;margin:30px auto 0;width:134px;height:42px}

/* blog */
.section-title{position:absolute;left:0;width:1200px;text-align:center;font:400 31px "Cinzel",Georgia,serif;color:var(--ink)}
.post{position:absolute;top:1870px;width:323px}
.post-img{height:207px}
.post h4{font:600 19px "Open Sans",Arial,sans-serif;color:var(--ink);margin-top:32px}
.post-meta{display:flex;align-items:center;gap:8px;font-size:13px;color:var(--muted);margin-top:10px}
.post-meta .sep{margin:0 6px}
.post p{font-size:13px;line-height:24px;margin-top:8px}
.post .more{display:block;margin-top:12px;font-weight:700;font-size:14px;color:var(--green)}

/* why */
.why-photo{position:absolute;left:0;top:2342px;width:711px;height:483px;background:linear-gradient(120deg,#bcd4ea,#6e99c2 40%,#2f5f8f 75%,#9fbfdc)}
.why-panel{position:absolute;left:711px;top:2342px;width:489px;height:483px;background:linear-gradient(135deg,#8cc63f,#7dbb3a 60%,#a6d36a)}
.why-panel h2{position:absolute;left:70px;top:52px;font:400 31px "Cinzel",Georgia,serif;color:var(--white)}
.why-panel .lead{position:absolute;left:70px;top:106px;width:360px;font-size:14px;line-height:24px;color:var(--white)}
.why-list{position:absolute;left:70px;top:186px;list-style:none}
.why-list li{display:flex;align-items:center;gap:12px;font-size:14px;line-height:25px;color:var(--white);white-space:nowrap}
.why-btn{left:70px;top:393px;width:131px;height:42px;background:transparent;border:2px solid var(--white)}

/* footer */
.foot-brand{position:absolute;left:98px;top:2970px;display:flex;align-items:center;gap:12px}
.foot-col{position:absolute;top:2908px}
.foot-col h5{font:400 19px "Cinzel",Georgia,serif;color:var(--ink);margin-bottom:22px;white-space:nowrap}
.foot-links{list-style:none;font-size:13px;line-height:24px;color:#444}
.foot-col p{font-size:13px;line-height:21px;color:#444}
.email-field{width:254px;border-bottom:1px solid #ccc;font-size:12px;color:#999;padding:12px 10px 8px;margin-top:6px}
.sub-btn{position:relative;display:flex;margin-top:14px;width:104px;height:34px;font-size:12px;border-radius:17px}
.contact-line{display:flex;gap:16px;font-size:13px;line-height:21px;color:#444;margin-bottom:22px;white-space:nowrap}
.foot-rule{position:absolute;left:98px;top:3124px;width:1004px;height:1px;background:var(--line)}
.copyright{position:absolute;left:98px;top:3153px;font-size:12px;color:#444}
.socials{position:absolute;left:976px;top:3147px;display:flex;gap:10px}
.socials span{width:26px;height:26px;border:1.5px solid var(--blue);border-radius:50%}
</style>
</head>
<body>

<header>
  <div class="brand"><span class="brand-mark"></span><span class="brand-name">VELUNORA</span></div>
  <div class="contact-item" style="left:491px">
    <span class="ring"><svg width="18" height="18" viewBox="0 0 24 24"><path fill="#8cc63f" d="M6.6 10.8a15 15 0 0 0 6.6 6.6l2.2-2.2c.3-.3.7-.4 1-.2 1.1.4 2.3.6 3.6.6.6 0 1 .4 1 1V20c0 .6-.4 1-1 1A17 17 0 0 1 3 4c0-.6.4-1 1-1h3.5c.6 0 1 .4 1 1 0 1.3.2 2.5.6 3.6.1.3 0 .7-.2 1z"/></svg></span>
    <span>Call us on : <b>1 555 014 2290</b></span>
  </div>
  <div class="contact-item" style="left:793px">
    <span class="ring"><svg width="18" height="18" viewBox="0 0 24 24"><path fill="#8cc63f" d="M3 5h18v14H3zM4 6.5v.4l8 5.3 8-5.3v-.4z"/></svg></span>
    <span>Email us : <b>info@velunora.de</b></span>
  </div>
  <nav class="main-nav">
    <a>Home</a><a>Philosophie</a><a>Diagnose</a><a>Therapie</a><a>Kontakt</a><a>Über uns</a><a>Zentrum</a><a>Unser Ergebnisse</a><a>Anfahrt</a>
  </nav>
</header>

<section class="hero">
  <div class="abs" role="img" aria-label="Gloved hand holding a red capsule over a molecular formula overlay" style="inset:0"></div>
  <h1 class="hero-title">Advanced<br>Laboratory<br>examination</h1>
  <div class="btn hero-btn">BOOK AN APPOINTMENT</div>
  <div class="slide-arrow" style="left:0"><svg width="14" height="22" viewBox="0 0 14 22"><path d="M11 2 3 11l8 9" stroke="#fff" stroke-width="3" fill="none"/></svg></div>
  <div class="slide-arrow" style="right:0"><svg width="14" height="22" viewBox="0 0 14 22"><path d="m3 2 8 9-8 9" stroke="#fff" stroke-width="3" fill="none"/></svg></div>
</section>

<section>
  <div class="welcome-box"></div>
  <h2 class="welcome-title">WELCOME TO VELUNORA</h2>
  <p class="welcome-text">Nam libero tempore, cum soluta nobis est eligendi optio cumquinihil<br>impedit quo minus id quod maxime placeat facere possimus, omnis<br>voluptas assumenda est, omnis dolor repellendus. Temporib autem<br>quibusdam et aut officiis debitis aut rerum necessitatibus saepe eve<br>niet ut et voluptates repudiandae sint et molestiae non recusandaea<br>que earum rerum hic tenetur a sapiente.</p>
  <div class="btn" style="left:143px;top:1025px;width:135px;height:42px">READ MORE</div>
  <div class="welcome-media" role="img" aria-label="Video still of a laboratory scientist with a digital brain analysis display"></div>
  <div class="play"><svg width="22" height="24" viewBox="0 0 22 24"><path d="M3 2l17 10L3 22z" fill="#fff"/></svg></div>
</section>

<section>
  <div class="feature-band"></div>
  <div class="feature" style="left:83px">
    <div class="feature-icon"><svg width="44" height="44" viewBox="0 0 24 24"><circle cx="12" cy="7.5" r="4.5" fill="#fff"/><path d="M3 21c0-5 4-8 9-8s9 3 9 8z" fill="#fff"/></svg></div>
    <h3>PHILOSOPHY</h3>
    <p>Nam libero tempore, cum soluta nobis est eligendi optio cumque nihil impedit quo minus id quod maxime placeat facere</p>
    <div class="btn">READ MORE</div>
  </div>
  <div class="feature" style="left:435px">
    <div class="feature-icon"><svg width="48" height="48" viewBox="0 0 24 24" fill="none" stroke="#fff"><circle cx="9" cy="14" r="4.5" stroke-width="3" stroke-dasharray="2.2 1.3"/><circle cx="9" cy="14" r="1.6" fill="#fff"/><circle cx="17" cy="7" r="3" stroke-width="2.4" stroke-dasharray="1.6 1"/></svg></div>
    <h3>APPROACH</h3>
    <p>Nam libero tempore, cum soluta nobis est eligendi optio cumque nihil impedit quo minus id quod maxime placeat facere</p>
    <div class="btn">READ MORE</div>
  </div>
  <div class="feature" style="left:787px">
    <div class="feature-icon"><svg width="40" height="44" viewBox="0 0 20 24"><path d="M2 1h11l5 5v17H2z" fill="#fff"/><path d="M5 11h10M5 14h10M5 17h10" stroke="#0455a3" stroke-width="1.4"/></svg></div>
    <h3>OUR RESULTS</h3>
    <p>Nam libero tempore, cum soluta nobis est eligendi optio cumque nihil impedit quo minus id quod maxime placeat facere</p>
    <div class="btn">READ MORE</div>
  </div>
</section>

<section>
  <h2 class="section-title" style="top:1788px">LATEST BLOG</h2>
  <article class="post" style="left:98px">
    <div class="post-img" role="img" aria-label="Scientist working with test tubes in a laboratory" style="background:linear-gradient(135deg,#2f6b9a,#8fb9d6 55%,#d9e7ef)"></div>
    <h4>Finibus Bonorum et Malorum</h4>
    <div class="post-meta"><svg width="12" height="12" viewBox="0 0 12 12"><rect x="1" y="2" width="10" height="9" fill="#0455a3"/></svg>25/09/2017<span class="sep">|</span><svg width="12" height="12" viewBox="0 0 24 24"><circle cx="12" cy="7" r="5" fill="#0455a3"/><path d="M2 23c0-6 4-9 10-9s10 3 10 9z" fill="#0455a3"/></svg>Elias</div>
    <p>Nemo enim ipsam voluptatem quia volupta asperna tur aut odit aut fugit, sed quia conseq.</p>
    <span class="more">READ MORE</span>
  </article>
  <article class="post" style="left:438px">
    <div class="post-img" role="img" aria-label="Doctor working at a digital medical display" style="background:linear-gradient(135deg,#dfe9ef,#a9c4d6 50%,#f2f5f7)"></div>
    <h4>Finibus Bonorum et Malorum</h4>
    <div class="post-meta"><svg width="12" height="12" viewBox="0 0 12 12"><rect x="1" y="2" width="10" height="9" fill="#0455a3"/></svg>25/09/2017<span class="sep">|</span><svg width="12" height="12" viewBox="0 0 24 24"><circle cx="12" cy="7" r="5" fill="#0455a3"/><path d="M2 23c0-6 4-9 10-9s10 3 10 9z" fill="#0455a3"/></svg>Elias</div>
    <p>Nemo enim ipsam voluptatem quia volupta asperna tur aut odit aut fugit, sed quia conseq.</p>
    <span class="more">READ MORE</span>
  </article>
  <article class="post" style="left:777px">
    <div class="post-img" role="img" aria-label="Doctor in consultation with an elderly patient" style="background:linear-gradient(135deg,#eef1f3,#b9c6cf 50%,#5a4a5e)"></div>
    <h4>Finibus Bonorum et Malorum</h4>
    <div class="post-meta"><svg width="12" height="12" viewBox="0 0 12 12"><rect x="1" y="2" width="10" height="9" fill="#0455a3"/></svg>25/09/2017<span class="sep">|</span><svg width="12" height="12" viewBox="0 0 24 24"><circle cx="12" cy="7" r="5" fill="#0455a3"/><path d="M2 23c0-6 4-9 10-9s10 3 10 9z" fill="#0455a3"/></svg>Elias</div>
    <p>Nemo enim ipsam voluptatem quia volupta asperna tur aut odit aut fugit, sed quia conseq.</p>
    <span class="more">READ MORE</span>
  </article>
</section>

<section>
  <div class="why-photo" role="img" aria-label="Medical research team looking at a transparent display"></div>
  <div class="why-panel">
    <h2>WHY CHOOSE US</h2>
    <p class="lead">Nam libero tempore, cum soluta nobis est eligendi optio cumque nihil impedit qu.</p>
    <ul class="why-list">
      <li><svg width="14" height="14" viewBox="0 0 14 14"><circle cx="7" cy="7" r="7" fill="#fff"/><path d="m3.8 7.2 2.2 2.2 4.2-4.4" stroke="#8cc63f" stroke-width="1.8" fill="none"/></svg>Minus id quodmaxi me placeat facere possim</li>
      <li><svg width="14" height="14" viewBox="0 0 14 14"><circle cx="7" cy="7" r="7" fill="#fff"/><path d="m3.8 7.2 2.2 2.2 4.2-4.4" stroke="#8cc63f" stroke-width="1.8" fill="none"/></svg>Omnis volupta assume nda est, omnis dolor</li>
      <li><svg width="14" height="14" viewBox="0 0 14 14"><circle cx="7" cy="7" r="7" fill="#fff"/><path d="m3.8 7.2 2.2 2.2 4.2-4.4" stroke="#8cc63f" stroke-width="1.8" fill="none"/></svg>Repellendu mporibus aum quibusdam et aut</li>
      <li><svg width="14" height="14" viewBox="0 0 14 14"><circle cx="7" cy="7" r="7" fill="#fff"/><path d="m3.8 7.2 2.2 2.2 4.2-4.4" stroke="#8cc63f" stroke-width="1.8" fill="none"/></svg>Ficiis debitis aut rerum necessitatibus saepe</li>
      <li><svg width="14" height="14" viewBox="0 0 14 14"><circle cx="7" cy="7" r="7" fill="#fff"/><path d="m3.8 7.2 2.2 2.2 4.2-4.4" stroke="#8cc63f" stroke-width="1.8" fill="none"/></svg>Eveniet ut et voluptates repudiandae sint etm</li>
      <li><svg width="14" height="14" viewBox="0 0 14 14"><circle cx="7" cy="7" r="7" fill="#fff"/><path d="m3.8 7.2 2.2 2.2 4.2-4.4" stroke="#8cc63f" stroke-width="1.8" fill="none"/></svg>Llestiae non recusandae. Itaque earum rerui</li>
      <li><svg width="14" height="14" viewBox="0 0 14 14"><circle cx="7" cy="7" r="7" fill="#fff"/><path d="m3.8 7.2 2.2 2.2 4.2-4.4" stroke="#8cc63f" stroke-width="1.8" fill="none"/></svg>Hic tenetur a sapiente delectus, ut aut reicien</li>
    </ul>
    <div class="btn why-btn">READ MORE</div>
  </div>
</section>

<footer>
  <div class="foot-brand"><span class="brand-mark"></span><span class="brand-name">VELUNORA</span></div>
  <div class="foot-col" style="left:433px">
    <h5>QUICK LINKS</h5>
    <ul class="foot-links"><li>Help</li><li>FAQ</li><li>Support</li><li>Sitemap</li><li>Terms Of Use</li><li>Privacy Statement</li></ul>
  </div>
  <div class="foot-col" style="left:610px">
    <h5>NEWSLETTER SUBSCRIPTION</h5>
    <p>Register your Email Address to get<br>information about us</p>
    <div class="email-field">Email Address</div>
    <div class="btn sub-btn">SUBSCRIBE</div>
  </div>
  <div class="foot-col" style="left:916px">
    <h5>CONTACT US</h5>
    <div class="contact-line"><svg width="12" height="16" viewBox="0 0 12 16"><path d="M6 0a6 6 0 0 0-6 6c0 4.5 6 10 6 10s6-5.5 6-10a6 6 0 0 0-6-6zm0 8.2A2.2 2.2 0 1 1 6 3.8a2.2 2.2 0 0 1 0 4.4z" fill="#0455a3"/></svg><span>7420 NW Harbor Lane Suite 118<br>Tampa, FL 33607</span></div>
    <div class="contact-line"><svg width="14" height="14" viewBox="0 0 24 24"><path fill="#0455a3" d="M6.6 10.8a15 15 0 0 0 6.6 6.6l2.2-2.2c.3-.3.7-.4 1-.2 1.1.4 2.3.6 3.6.6.6 0 1 .4 1 1V20c0 .6-.4 1-1 1A17 17 0 0 1 3 4c0-.6.4-1 1-1h3.5c.6 0 1 .4 1 1 0 1.3.2 2.5.6 3.6.1.3 0 .7-.2 1z"/></svg><span>1 555 014 2290</span></div>
    <div class="contact-line"><svg width="14" height="14" viewBox="0 0 24 24"><path fill="#0455a3" d="M2 5h20v14H2zM3 6.5v.4l9 5.3 9-5.3v-.4z"/></svg><span>info@velunora.de</span></div>
  </div>
  <div class="foot-rule"></div>
  <p class="copyright">Copyrights © 2018, Velunora.&nbsp; All rights reserved.</p>
  <div class="socials"><span></span><span></span><span></span><span></span></div>
</footer>

</body>
</html>
```